Print on top the name of the company: (Or Similar)
Larkmoor Cleaning & Disinfecting
Because your standards aren't standard.

We adhere to ALL NVB guidelines for both residential and commercial cleaning.

Infection Control is our ultimate goal.

Instructions:
Opening a residential and commercial cleaning and disinfecting company in south Florida.

Targeting high-end residential clients, commercial and healthcare facilities, specializing in Ambulatory Care Guidelines. With a concentration and expertise in targeting Covid 19 and other transmissible pathogens.

UMRE trained.
Owned and operated by a licensed BSN Registered Nurse specially ​trained in Infection Control Prevention with over 25 years experience. Over two decades in Ambulatory Surgery Center Administration, Director of Nursing and Infection Control Prevention ad Consulting.

Looking to create a business flier that emphasizes Cleaning & Disinfection
along with the standard expectation for residential and Commercial cleaning services
Updates

Need extra days to review

Target Market(s)

Residential & Commercial

Font styles to use
Decorative

Requirements
Must have
• A checklist for cleaning services

```html
<!DOCTYPE html>
<html lang="en">
<head>
<meta charset="utf-8">
<title>Larkmoor Cleaning &amp; Disinfecting – Flyer</title>
<link rel="stylesheet" href="https://fonts.googleapis.com/css2?family=Rubik:wght@400;500;600;700;800;900&display=swap">
<style>
  :root {
    --orange: #ec9125;
    --ink: #111111;
    --charcoal: #3a3a3c;
    --paper: #ececec;
    --paper-shade: #d9d9d9;
    --backdrop: #e4e4e4;
    --white: #ffffff;
    --photo-blue: #2f4f9a;
    --photo-grey: #8c8f94;
  }
  * { box-sizing: border-box; margin: 0; padding: 0; }
  html, body {
    width: 1200px; height: 1021px; overflow: hidden;
    background: var(--backdrop);
    font-family: "Rubik", sans-serif;
  }
  .flyer {
    position: absolute; left: 260px; top: 30px;
    width: 680px; height: 960px;
    background: linear-gradient(180deg, var(--paper) 0%, var(--paper-shade) 100%);
    box-shadow: 0 18px 40px rgba(0,0,0,.18);
    overflow: hidden;
  }
  .flyer__shapes { position: absolute; inset: 0; }
  .brand { position: absolute; left: 44px; top: 44px; width: 330px; }
  .brand__name {
    font-weight: 900; font-size: 60px; line-height: .95; color: var(--ink);
    letter-spacing: .5px; text-transform: uppercase;
  }
  .brand__rule {
    height: 3px; width: 260px; margin: 14px 0 12px 20px;
    background: linear-gradient(90deg, transparent, var(--charcoal) 40%, transparent);
  }
  .brand__tagline { font-weight: 600; font-size: 21px; line-height: 1.18; color: var(--ink); }
  .intro { position: absolute; left: 0; right: 0; top: 340px; text-align: center; }
  .intro__lead { font-weight: 700; font-size: 14.5px; color: var(--ink); }
  .intro__goal {
    margin-top: 6px; font-weight: 600; font-size: 29px; color: var(--orange);
    text-transform: uppercase; letter-spacing: .3px;
  }
  .facts {
    position: absolute; left: 30px; right: 30px; top: 428px;
    display: grid; grid-template-columns: 1fr 1fr 1.15fr; column-gap: 26px;
  }
  .facts__item { font-size: 12.5px; line-height: 1.3; text-align: center; color: var(--ink); }
  .services { position: absolute; text-align: center; color: var(--white); }
  .services--commercial { left: 0; top: 628px; width: 350px; }
  .services--residential { left: 350px; top: 670px; width: 330px; }
  .services__title { font-weight: 800; font-size: 22px; text-transform: uppercase; margin-bottom: 8px; }
  .services__list { list-style: none; font-weight: 600; font-size: 14px; line-height: 1.25; }
  .call { position: absolute; left: 0; right: 0; top: 882px; text-align: center; color: var(--ink); }
  .call__text { font-weight: 700; font-size: 20px; }
  .call__phone { font-weight: 800; font-size: 34px; line-height: 1.15; letter-spacing: .5px; }
</style>
</head>
<body>
<article class="flyer">
  <svg class="flyer__shapes" width="680" height="960" viewBox="0 0 680 960">
    <defs>
      <linearGradient id="photoFill" x1="0" y1="0" x2="1" y2="1">
        <stop offset="0" stop-color="var(--photo-grey)"/>
        <stop offset=".55" stop-color="var(--photo-blue)"/>
        <stop offset="1" stop-color="#c9b07a"/>
      </linearGradient>
    </defs>
    <polygon class="header-band" points="0,0 415,0 330,322 0,272" fill="var(--orange)"/>
    <polygon class="header-photo" role="img" aria-label="Photo of a cleaner in a blue uniform carrying a caddy of cleaning supplies" points="415,0 680,0 680,228 330,322" fill="url(#photoFill)"/>
    <polygon class="header-accent" points="330,322 680,228 680,300" fill="var(--charcoal)"/>
    <line class="facts-divider" x1="236" y1="422" x2="222" y2="580" stroke="var(--charcoal)" stroke-width="1.2"/>
    <line class="facts-divider" x1="448" y1="428" x2="434" y2="596" stroke="var(--charcoal)" stroke-width="1.2"/>
    <polygon class="panel-commercial" points="0,605 350,605 350,862 0,838" fill="var(--ink)"/>
    <polygon class="panel-residential" points="350,650 680,650 680,880 350,862" fill="var(--orange)"/>
  </svg>

  <header class="brand">
    <h1 class="brand__name">Larkmoor Cleaning</h1>
    <div class="brand__rule"></div>
    <p class="brand__tagline">Larkmoor Cleaning &amp; Disinfecting Because your standards aren't standard.</p>
  </header>

  <section class="intro">
    <p class="intro__lead">We adhere to ALL NVB guidelines for both residential and commercial cleaning.</p>
    <h2 class="intro__goal">Infection control is our ultimate goal.</h2>
  </section>

  <section class="facts">
    <p class="facts__item">INSTRUCTIONS:<br>Opening a residential and commercial cleaning and disinfecting company in south Florida.</p>
    <p class="facts__item">Targeting high-end residential clients, commercial and healthcare facilities, specializing in Ambulatory Care Guidelines. With a concentration and expertise in targeting Covid 19 and other transmissible pathogens.</p>
    <p class="facts__item">UMRE TRAINED.<br>Owned and operated by a licensed BSN Registered Nurse specially trained in Infection Control Prevention with over 25 years experience. Over two decades in Ambulatory Surgery Center Administration, Director of Nursing and Infection Control Prevention ad Consulting.</p>
  </section>

  <section class="services services--commercial">
    <h3 class="services__title">Commercial</h3>
    <ul class="services__list">
      <li>Janitorial</li><li>Offices</li><li>Floor maintenance</li><li>Carpet cleaning</li>
      <li>Move-ins</li><li>Move-outs</li><li>Construction clean-ups</li><li>Estate clean-outs</li>
    </ul>
  </section>

  <section class="services services--residential">
    <h3 class="services__title">Residential</h3>
    <ul class="services__list">
      <li>House cleaning</li><li>Before and after party</li><li>Move-ins</li><li>Move-outs</li>
      <li>Holiday cleaning</li><li>Seasonal cleaning</li><li>Carpet cleaning</li><li>Deodorizing and sanitizing</li>
    </ul>
  </section>

  <footer class="call">
    <p class="call__text">Call us to find out how you can save money this month!</p>
    <p class="call__phone">(305) 555 01 48</p>
  </footer>
</article>
</body>
</html>
```